Chicken Wing A0 and A4 Poster

Our restaurant name is Tovvra Grill

We have introduced chicken wings to our menu. They are deep fried and mixed with different sauce selections.

The sauce options are: Tovvra BBQ, Regular BBQ, Sweet Chili and Garlic, Hot Chili, Garlic

Available in a 6, 10 or 20 Pack.
Larger Catering Packs Available

We have uploaded some pictures from the internet with chicken wings.

We also have 4 other poster designs coming in the next 3 weeks.

Industry/Entity Type

Restaurant

```html
<!DOCTYPE html>
<html lang="en">
<head>
<meta charset="utf-8">
<title>Tovvra Grill – Chicken Wings Poster</title>
<link href="https://fonts.googleapis.com/css2?family=Bebas+Neue&family=Gochi+Hand&display=swap" rel="stylesheet">
<style>
  :root {
    --page-bg: #2b2b2e;
    --pink: #e2187f;
    --magenta: #b01782;
    --purple: #7a1670;
    --night: #0d0a0c;
    --white: #ffffff;
    --ink: #111111;
    --orange: #f7931e;
    --plate: #f2f0ee;
    --wing-dark: #8a3410;
    --wing-light: #d9722a;
  }
  * { box-sizing: border-box; margin: 0; padding: 0; }
  html, body { width: 1200px; height: 1000px; overflow: hidden; }
  body { background: var(--page-bg); position: relative; font-family: "Bebas Neue", sans-serif; }

  .poster {
    position: absolute; left: 282px; top: 78px; width: 608px; height: 862px;
    overflow: hidden; border: 2px solid var(--white);
    background: linear-gradient(180deg, var(--pink) 0%, var(--pink) 38%, var(--magenta) 62%, var(--purple) 78%, var(--night) 92%);
  }

  .social-bar {
    position: absolute; top: 16px; left: 0; width: 100%;
    display: flex; justify-content: center; gap: 52px;
    color: var(--white); font-size: 20px; letter-spacing: 0.5px;
  }
  .social-item { display: flex; align-items: center; gap: 8px; }
  .social-dot { width: 14px; height: 14px; border-radius: 50%; background: var(--orange); }

  .headline { position: absolute; top: 88px; left: 144px; width: 440px; color: var(--white); white-space: nowrap; }
  .headline-line {
    font-size: 44px; line-height: 1;
    text-shadow: 2px 2px 0 var(--ink), -1px -1px 0 var(--ink), 1px -1px 0 var(--ink), -1px 1px 0 var(--ink);
  }
  .headline-line--wide { font-size: 42px; }
  .headline-feature {
    font-family: "Gochi Hand", cursive; color: var(--orange);
    font-size: 64px; line-height: 1; margin: 2px 0 4px -2px;
    text-shadow: 2px 2px 0 var(--ink), -1px -1px 0 var(--ink), 1px -1px 0 var(--ink), -1px 1px 0 var(--ink);
  }

  .dish-photo {
    position: absolute; left: 0; top: 250px; width: 604px; height: 430px;
  }

  .delivery-badge {
    position: absolute; left: 290px; top: 350px; width: 162px; height: 162px;
    border-radius: 50%; border: 3px solid var(--ink);
    background: radial-gradient(circle at 40% 35%, #c21d9a, #7d1468);
    color: var(--white); text-align: center;
    display: flex; flex-direction: column; justify-content: center;
  }
  .delivery-label {
    font-size: 28px; line-height: 0.95;
    text-shadow: 2px 2px 0 var(--ink), -1px -1px 0 var(--ink);
  }
  .delivery-phone { font-size: 30px; margin-top: 12px; }

  .brand { position: absolute; left: 0; top: 690px; width: 100%; text-align: center; }
  .brand-row { display: inline-flex; align-items: center; gap: 12px; }
  .brand-name { font-size: 78px; color: var(--pink); line-height: 1; letter-spacing: 1px; }
  .brand-mark { width: 26px; height: 26px; border-radius: 50%; background: var(--pink); }
  .brand-tagline { font-size: 22px; color: var(--pink); letter-spacing: 3px; margin-top: 2px; }
</style>
</head>
<body>
  <main class="poster">
    <header class="social-bar">
      <span class="social-item"><span class="social-dot"></span>FB.COM/TOVVRA</span>
      <span class="social-item"><span class="social-dot"></span>@TOVVRA</span>
      <span class="social-item">
        <svg width="18" height="18" viewBox="0 0 18 18" aria-hidden="true">
          <circle cx="9" cy="9" r="8" fill="none" stroke="#f7931e" stroke-width="1.8"/>
          <ellipse cx="9" cy="9" rx="3.5" ry="8" fill="none" stroke="#f7931e" stroke-width="1.5"/>
          <line x1="1" y1="9" x2="17" y2="9" stroke="#f7931e" stroke-width="1.5"/>
        </svg>WWW.TOVVRA.COM</span>
    </header>

    <section class="headline">
      <p class="headline-line">DELICIOUS</p>
      <p class="headline-feature">Chicken Wings</p>
      <p class="headline-line headline-line--wide">THAT WONT HURT YOUR WALLET</p>
    </section>

    <svg class="dish-photo" viewBox="0 0 604 430" role="img" aria-label="Photo of glazed chicken wings on a white plate with herbs and dip">
      <defs>
        <radialGradient id="wingsTone" cx="45%" cy="45%" r="60%">
          <stop offset="0%" stop-color="#d9722a"/>
          <stop offset="100%" stop-color="#8a3410"/>
        </radialGradient>
      </defs>
      <ellipse cx="290" cy="247" rx="295" ry="175" fill="#f2f0ee"/>
      <ellipse cx="290" cy="185" rx="270" ry="165" fill="url(#wingsTone)"/>
    </svg>

    <div class="delivery-badge">
      <span class="delivery-label">DELIVERY<br>SERVICE</span>
      <span class="delivery-phone">555-018273</span>
    </div>

    <footer class="brand">
      <div class="brand-row">
        <span class="brand-name">Tovvra Grill</span>
        <span class="brand-mark"></span>
      </div>
      <p class="brand-tagline">AUTHENTIC LEBANESE FOOD</p>
    </footer>
  </main>
</body>
</html>
```